HOLLOWAY PINE SERVICES INC. | ||
HOLLOWAY PINE SERVICES INC.COM | ||
Cutting-Edge Corporate Modern Professional |
Lionel Fabre | ||
HOLLOWAY PINE SERVICESINC. | ||
There is no address! Thank you | ||
HOLLOWAYPINESERVICESINC@ORVELMAIL.COM | ||
HOLLOWAYPINESERVICESINC.COM | ||
I want my logo to be used with all my stationary. Thank You. | ||
Im open to anything that looks good | ||
Logo_4353.jpg i like for my stationary to have a light colored look1 not a dark color tint. light n ritch in color |

```html
<!DOCTYPE html>
<html lang="en">
<head>
<meta charset="utf-8">
<title>Holloway Pine Services Inc. – Business Card</title>
<link rel="stylesheet" href="https://fonts.googleapis.com/css2?family=Open+Sans:ital,wght@0,400;0,600;0,700;1,400&display=swap">
<style>
  :root {
    --stage: #202020;
    --card-white: #ffffff;
    --card-grain: #ececec;
    --green-light: #8fc43f;
    --green: #5fa22a;
    --green-dark: #2f7a1c;
    --green-deep: #2d6a18;
    --text-white: #ffffff;
    --logo-green: #4f9a22;
  }
  * { margin: 0; padding: 0; box-sizing: border-box; }
  html, body { width: 1200px; height: 923px; overflow: hidden; }
  body {
    background: var(--stage);
    font-family: "Open Sans", Arial, sans-serif;
    position: relative;
  }
  .card {
    position: absolute;
    overflow: hidden;
    background: linear-gradient(90deg, var(--card-white) 0%, var(--card-grain) 30%, var(--card-white) 55%, var(--card-grain) 80%, var(--card-white) 100%);
  }
  .card-front { left: 125px; top: 95px; width: 586px; height: 337px; }
  .card-back  { left: 499px; top: 482px; width: 591px; height: 375px; }

  .grain {
    position: absolute; left: 0; top: 0; width: 100%; height: 100%;
    background: linear-gradient(180deg, rgba(255,255,255,0.6), rgba(230,230,230,0.4));
  }
  .green-band {
    position: absolute; left: 0; right: 0; bottom: 0;
    background: linear-gradient(180deg, var(--green-light) 0%, var(--green) 45%, var(--green-dark) 100%);
  }
  .card-front .green-band { top: 224px; }
  .card-back  .green-band { top: 267px; }

  .tagline {
    position: absolute; top: 14px; left: 0; right: 0;
    text-align: center; font-style: italic; font-size: 12px;
    color: var(--green);
  }
  .logo-mark {
    position: absolute; border-radius: 50%;
    background: var(--green);
  }
  .card-front .logo-mark { width: 62px; height: 62px; left: 262px; top: 52px; }
  .card-back  .logo-mark { width: 86px; height: 86px; left: 252px; top: 82px; }

  .company-name {
    position: absolute; left: 0; right: 0; text-align: center;
    font-weight: 700; color: var(--logo-green); line-height: 1.05;
    text-transform: uppercase;
  }
  .card-front .company-name { top: 122px; font-size: 22px; }
  .card-back  .company-name { top: 176px; font-size: 14px; }

  .name-banner {
    position: absolute; left: 173px; top: 200px; width: 240px; height: 40px;
    background: linear-gradient(180deg, var(--green), var(--green-deep));
    color: var(--text-white); font-weight: 700; font-size: 24px;
    text-align: center; line-height: 40px;
    clip-path: polygon(4% 0, 100% 0, 96% 100%, 0 100%);
  }
  .services {
    position: absolute; left: 20px; right: 20px; top: 250px;
    text-align: center; color: var(--text-white); font-size: 10.5px; line-height: 15px;
  }
  .services span::before { content: "• "; color: var(--green-light); }

  .contact {
    position: absolute; bottom: 30px; color: var(--text-white);
    font-size: 11.5px; line-height: 19px;
  }
  .contact-phone { left: 22px; }
  .contact-online { right: 22px; text-align: right; }
</style>
</head>
<body>

  <section class="card card-front" aria-label="Business card front">
    <div class="grain" role="img" aria-label="Brushed white texture"></div>
    <p class="tagline">A not for profit medical marijuana collective</p>
    <div class="logo-mark"></div>
    <p class="company-name">Holloway Pine Services<br>Inc.com</p>
    <div class="green-band"></div>
    <div class="name-banner">Lionel Fabre</div>
    <p class="services">
      <span>Operating in Strict Compliance With Ca. Prop 215 &amp; Sb 420</span><br>
      <span>Qualified Patients Only</span> <span>Speedy Delivery Service</span> <span>Concentrates &amp; Edibles</span><br>
      <span>Ask about our Rewards Card Free Gram after 8 visits with $20 donations</span><br>
      <span>Open Monday-Sunday 8am-8pm</span>
    </p>
  </section>

  <section class="card card-back" aria-label="Business card back">
    <div class="grain" role="img" aria-label="Brushed white texture"></div>
    <div class="logo-mark"></div>
    <p class="company-name">Holloway Pine Services Inc.</p>
    <div class="green-band"></div>
    <p class="contact contact-phone">Ph: (555)014-2270<br>Cell: (555)017-9386</p>
    <p class="contact contact-online">Email: hollowaypineservicesinc@orvelmail.com<br>Web : hollowaypineservicesinc.com</p>
  </section>

</body>
</html>
```